Business Card Design

I need a business card, for my company that reflects fire and building.
I am a bushfire consultant, and my role is to determine a fire assessment for new houses being built, in bushfire prone areas.
Compiling a report on what building materials will need to be used, and whether or not parts of the block will need to be cleared of vegetation. I would like to see the colours of fire, and possibly a house on there as well, or maybe just fire. This will probably be used as a logo as well, and will reflect the severity of fire to housing.
Target Market(s)
New home builders residential
Industry/Entity Type
Building
Contact Information for Business Card
Emberline Advisory Coastal Range
Bushfire Consultant
Garth Pemberly
0438 261 904

```html
<!DOCTYPE html>
<html lang="en">
<head>
<meta charset="utf-8">
<title>Emberline Advisory Coastal Range — Business Card</title>
<link rel="stylesheet" href="https://fonts.googleapis.com/css2?family=Open+Sans:wght@400;700&display=swap">
<style>
  :root {
    --canvas: #e7e4df;
    --card-dark: #141414;
    --card-dark-edge: #050505;
    --card-light: #fbfbfa;
    --ink: #1b1b1b;
    --ink-soft: #2c2c2c;
    --ember-red: #d42a26;
    --flame-gold: #e9ab1c;
    --white: #ffffff;
  }
  * { box-sizing: border-box; margin: 0; padding: 0; }
  html, body {
    width: 1200px;
    height: 1023px;
    overflow: hidden;
  }
  body {
    background: var(--canvas);
    font-family: "Open Sans", Arial, sans-serif;
    display: flex;
    flex-direction: column;
    align-items: center;
    justify-content: center;
    gap: 70px;
  }
  .card {
    width: 600px;
    height: 340px;
    border-radius: 4px;
    box-shadow: 0 10px 28px rgba(0, 0, 0, 0.22);
    position: relative;
  }

  /* Front face */
  .card--front {
    background: linear-gradient(160deg, #262626 0%, var(--card-dark) 45%, var(--card-dark-edge) 100%);
    display: flex;
    align-items: center;
    justify-content: center;
  }
  .brand {
    display: flex;
    align-items: center;
    gap: 14px;
  }
  .brand__mark {
    width: 22px;
    height: 22px;
    background: var(--ember-red);
    flex: none;
  }
  .brand__name {
    font-weight: 700;
    text-transform: uppercase;
    line-height: 1.1;
    letter-spacing: 0.01em;
  }
  .card--front .brand__name {
    color: var(--white);
    font-size: 30px;
  }

  /* Back face */
  .card--back {
    background: var(--card-light);
    display: grid;
    grid-template-columns: 1fr 1px 1fr;
    align-items: center;
    padding: 60px 0;
  }
  .card--back .brand {
    justify-self: center;
    padding-left: 20px;
  }
  .card--back .brand__mark {
    width: 16px;
    height: 16px;
  }
  .card--back .brand__name {
    color: var(--ink);
    font-size: 19px;
  }
  .divider {
    height: 100%;
    background: var(--flame-gold);
  }
  .contact {
    padding-left: 50px;
    color: var(--ink-soft);
  }
  .contact__name {
    font-weight: 700;
    font-size: 21px;
    color: var(--ink);
    margin-bottom: 4px;
  }
  .contact__role {
    font-size: 16px;
    margin-bottom: 4px;
  }
  .contact__phone {
    display: flex;
    align-items: center;
    gap: 4px;
    font-size: 16px;
  }
  .contact__phone svg { width: 14px; height: 14px; flex: none; }
</style>
</head>
<body>
  <section class="card card--front" aria-label="Business card front">
    <div class="brand">
      <span class="brand__mark"></span>
      <span class="brand__name">Emberline Advisory<br>Coastal Range</span>
    </div>
  </section>

  <section class="card card--back" aria-label="Business card back">
    <div class="brand">
      <span class="brand__mark"></span>
      <span class="brand__name">Emberline Advisory<br>Coastal Range</span>
    </div>
    <div class="divider"></div>
    <div class="contact">
      <p class="contact__name">Garth Pemberly</p>
      <p class="contact__role">Bushfire Consultant</p>
      <p class="contact__phone">
        <svg viewBox="0 0 24 24" aria-hidden="true">
          <path fill="#e9ab1c" d="M6.6 10.8a15.1 15.1 0 0 0 6.6 6.6l2.2-2.2c.3-.3.7-.4 1-.2 1.1.4 2.3.6 3.6.6.6 0 1 .4 1 1V20c0 .6-.4 1-1 1A17 17 0 0 1 3 4c0-.6.4-1 1-1h3.5c.6 0 1 .4 1 1 0 1.3.2 2.5.6 3.6.1.3 0 .7-.2 1z"/>
        </svg>
        <span>: 0438 261 904</span>
      </p>
    </div>
  </section>
</body>
</html>
```